Church needs a graphic design/flyer layout for upcoming series

I need a multi-purpose design for promoting both our upcoming series of messages and our fall kick-off event where we will launch the messages.

Our promotion will be printed on a two-sided. One side is simple and focuses on the series and the other side has details in regards to the event. I have provided an attachment example of what we did last time.

The design needs to be multi-purpose because it will be used for our sermon Power Points, placed on our website banner, social media, etc.

• Sermon series is called “Harbor Lanterns”
• The subtitle will be “What’s keeping you from God?”
• Our name logo should be on the graphic as well.
• The subject manner will revolve around common hurdles that people face about God and Christianity: The existence of God, the exclusivity of religion, Hell, the reliability of the Bible, Hypocrisy in the church, etc.
• Our mission is “Connecting Young Families to Christ” so our focus is to reach out to families while not being exclusive to others.
• Our target audience is families with school-aged kids.
• This series is an invitational focus so we want it to be appealing to non-church goers.
• It should be attention grabbing while not being too ‘edgy’

• The front of the card will most likely consist the Sermon Series Graphic, title & subtitle of the series, and perhaps our name logo somewhere on it.
• The back of the card will invite and give the basic information for the event so that the people will be encouraged to save the date and come to the event.
• Here are some things that could be included on that advertisement:
o The name of the event: “Westbrook Commons Open Day”
o The date and time of the event: Sept 23rd @ 10:30
o Features of the event:
 Free lunch
 Children’s program
 Bouncy Castle
 Start of the “Harbor Lanterns” messages.
 Sample of topics
o Information about the church: our website and address, etc
o Engaging pictures and graphics.
• The rest of the tone and manner are the same as the sermon series graphic.
The flyer will be 11X14, like a postcard size.

Target Market(s)

Young families who are spiritually curious but not committed church attenders.

Colors

Designer to choose colors to be used in the design.

Requirements
Nice to have
• A modern and professional looking design.
Should not have
• Anything offensive or not family friendly.

```html
<!DOCTYPE html>
<html lang="en">
<head>
<meta charset="utf-8">
<title>Harbor Lanterns – Westbrook Commons Open Day Postcard</title>
<link rel="stylesheet" href="https://fonts.googleapis.com/css2?family=Playfair+Display:wght@700&family=Oswald:wght@300;400;500&family=Caveat+Brush&family=Libre+Baskerville&display=swap">
<style>
  :root {
    --page-bg: #e4e4e4;
    --sun-light: #f8d65a;
    --sun-mid: #f2a531;
    --sun-deep: #e06a22;
    --ember: #c8421f;
    --title-dark: #5a2416;
    --title-warm: #d2562a;
    --plum: #4e2450;
    --plum-deep: #2f1a3a;
    --dusk: #8a3a5e;
    --paper: #ffffff;
    --mist: #d9d9db;
    --ink: #1d1d1f;
    --muted: #555558;
  }
  * { box-sizing: border-box; margin: 0; padding: 0; }
  html, body {
    width: 1054px; height: 1200px; overflow: hidden;
    background: var(--page-bg);
  }
  .card {
    position: absolute; left: 194px; width: 666px;
    overflow: hidden;
    box-shadow: 0 3px 10px rgba(0,0,0,.18);
  }

  /* Front: series card */
  .card--front { top: 64px; height: 521px; }
  .front__art {
    position: absolute; inset: 0;
    background:
      radial-gradient(ellipse at 48% 30%, var(--sun-light) 0%, var(--sun-mid) 38%, transparent 70%),
      linear-gradient(180deg, var(--sun-mid) 0%, var(--sun-deep) 60%, var(--ember) 100%);
  }
  .front__title {
    position: absolute; top: 160px; left: 0; right: 0;
    text-align: center;
    font-family: "Playfair Display", serif; font-weight: 700;
    font-size: 74px; line-height: .98; letter-spacing: 1px;
    color: var(--title-dark);
  }
  .front__title span { display: block; }
  .front__title span:last-child { color: var(--title-warm); }
  .front__subtitle {
    position: absolute; top: 318px; left: 0; right: 0; text-align: center;
    font-family: "Caveat Brush", cursive; font-size: 27px;
    color: var(--plum-deep); letter-spacing: .5px;
  }
  .front__brand {
    position: absolute; top: 412px; left: 0; right: 0; text-align: center;
  }
  .brand-dot {
    display: block; margin: 0 auto 4px;
    width: 30px; height: 30px; border-radius: 50%;
    background: var(--plum-deep);
  }
  .front__brand .brand-name {
    font-family: "Libre Baskerville", serif; font-size: 10px; color: var(--plum-deep);
  }

  /* Back: event card */
  .card--back { top: 612px; height: 524px; background: var(--paper); }
  .back__panel { position: absolute; inset: 0; }
  .back__hills-light {
    position: absolute; right: 0; bottom: 0; width: 330px; height: 220px;
    background: linear-gradient(180deg, var(--paper) 0%, var(--mist) 100%);
  }
  .back__title {
    position: absolute; top: 62px; left: 0; width: 410px; text-align: center;
    font-family: "Playfair Display", serif; font-weight: 700;
    font-size: 48px; line-height: 1; color: var(--paper); text-transform: uppercase;
  }
  .back__date {
    position: absolute; top: 270px; left: 0; width: 410px; text-align: center;
    font-family: "Caveat Brush", cursive; font-size: 22px; color: var(--paper);
  }
  .features {
    position: absolute; top: 318px; left: 0; width: 410px; text-align: center;
    font-family: "Oswald", sans-serif; color: var(--paper); list-style: none;
  }
  .features__lead { font-weight: 300; font-size: 16px; margin-bottom: 3px; }
  .features li { font-weight: 400; font-size: 17px; line-height: 23px; text-transform: uppercase; }
  .contact {
    position: absolute; top: 152px; right: 28px; text-align: right;
    font-family: "Oswald", sans-serif; color: var(--ink);
  }
  .contact dt { font-size: 11px; font-weight: 400; color: var(--muted); text-transform: uppercase; letter-spacing: .4px; }
  .contact dd { font-size: 15px; font-weight: 500; line-height: 17px; text-transform: uppercase; margin-bottom: 21px; }
  .back__brand {
    position: absolute; top: 416px; left: 440px; width: 200px; text-align: center;
  }
  .back__brand .brand-dot { width: 48px; height: 48px; background: var(--plum); margin-bottom: 6px; }
  .back__brand .brand-name { font-family: "Libre Baskerville", serif; font-size: 12px; color: var(--ink); }
</style>
</head>
<body>

<section class="card card--front">
  <div class="front__art" role="img" aria-label="Warm sunset sky over mountains with a man looking upward and a tall cross silhouette"></div>
  <h1 class="front__title"><span>HARBOR</span><span>LANTERNS</span></h1>
  <p class="front__subtitle">WHAT'S KEEPING YOU FROM GOD?</p>
  <div class="front__brand">
    <span class="brand-dot"></span>
    <span class="brand-name">Alder Grove Family Church</span>
  </div>
</section>

<section class="card card--back">
  <div class="back__hills-light" role="img" aria-label="Faint grey mountain range"></div>
  <svg class="back__panel" width="666" height="524" viewBox="0 0 666 524">
    <defs>
      <linearGradient id="plumFade" x1="0" y1="0" x2="0" y2="1">
        <stop offset="0" stop-color="#4e2450"/>
        <stop offset=".55" stop-color="#4a2350"/>
        <stop offset=".75" stop-color="#8a3a5e"/>
        <stop offset="1" stop-color="#2f1a3a"/>
      </linearGradient>
    </defs>
    <polygon points="0,0 460,0 391,524 0,524" fill="url(#plumFade)" role="img" aria-label="Purple dusk sky with layered mountain silhouettes and setting sun"/>
  </svg>
  <h2 class="back__title">Westbrook<br>Commons<br>Open Day</h2>
  <p class="back__date">SEPT 23RD @ 10:30</p>
  <ul class="features">
    <li class="features__lead" style="text-transform:none">Features of the event:</li>
    <li>Free Lunch</li>
    <li>Children's Program</li>
    <li>Bouncy Castle</li>
    <li>Start of the “Harbor Lanterns” Messages</li>
    <li>Sample of Topics</li>
  </ul>
  <dl class="contact">
    <dt>Location</dt>
    <dd>1185 Maple Ridge Road<br>Brantwood, ON K2M 4R8</dd>
    <dt>Phone</dt>
    <dd>+ 1 555.014.2290</dd>
    <dt>Email</dt>
    <dd>info@aldergrovechurch.ca</dd>
    <dt>Website</dt>
    <dd>www.aldergrovechurch.ca</dd>
  </dl>
  <div class="back__brand">
    <span class="brand-dot"></span>
    <span class="brand-name">Alder Grove Family Church</span>
  </div>
</section>

</body>
</html>
```